Roofing & Siding door hanger flyer

-Looking to make door hanger flyer for Pellmont Roofing & Siding
-4.5" wide x 11" tall
-2 sided full colour
-We have started a new website (the content is changing) I have attached photos.
-About us:
-25 year labour warranty's available
-32 years in Calgary
-QCR A+ Member
-NWTG (Prairie Joint Shingle Guild) (logo attached)
-KOV Summit Select (logo attached)
-Owen Brisket (logo attached)
-Slogan "Raised On Care, Proven Through Seasons" 32 years in Calgary
-Sale
-Page 1 & 2 design ideas
We are in your area, contact us today for your Exclusive limited time offer! *discounts apply exclusively to new agreements only
Updates
-Please keep simple, clean & bright
-I really like the bright blue from our new logo (new logo uploaded)
-We specialize in Roofing -Siding-Gutters & full Exterior Renos (like the competitor example uploaded)
-This is the NEW website we are currently working on (not finished) https://mockview.example-draftpad.net/view/1a2b3c4d-5e6f-4a7b-8c9d-0e1f2a3b4c5d-7k2m/?fullscreen
-This is our OLD website https://pellmontshingleworks.com
-For the sale "We are in your area, contact us today for your Exclusive limited time offer" *discounts apply exclusively to new agreements only
-Free Estimates
-our phone# is 403-555-0148
-our website is pellmontshingleworks.com
-keep simple, clean, bright use the "new logo" uploaded. Check out the competitor example uploaded file
-We are in your area, Contact us today for your Exclusive limited time offer! *discounts apply to new agreements only
-FREE ESTIMATES
-Specialized in Roofing /Siding /Gutters Full Exterior Reno's
-We are currently working on a NEW website https://mockview.example-draftpad.net/view/1a2b3c4d-5e6f-4a7b-8c9d-0e1f2a3b4c5d-7k2m/?fullscreen
-Our OLD website https://pellmontshingleworks.com/
-Post old site address on flyer pellmontshingleworks.com
-Phone # 403-555-0148
Target Market(s)
40-55
Industry/Entity Type
Roofing Siding & full Exterior Reno's
Look and feel

```html
<!DOCTYPE html>
<html lang="en">
<head>
<meta charset="utf-8">
<title>Pellmont Roofing &amp; Siding – Door Hanger</title>
<link href="https://fonts.googleapis.com/css2?family=Poppins:wght@500;600;700;800;900&display=swap" rel="stylesheet">
<style>
:root{
  --blue:#0667be;
  --blue-dark:#0553a0;
  --red:#e8141b;
  --black:#0b0b0b;
  --ink:#1a1a1a;
  --white:#ffffff;
  --stage:#e8e8e8;
  --paper:#ffffff;
}
*{box-sizing:border-box;margin:0;padding:0}
html,body{width:703px;height:1200px;overflow:hidden}
body{position:relative;background:var(--paper);font-family:"Poppins",sans-serif;color:var(--ink)}
.stage-top{position:absolute;left:0;top:0;width:703px;height:598px;background:var(--stage)}
.hanger{position:absolute;width:214px;height:524px;background:var(--white);overflow:hidden;box-shadow:0 3px 10px rgba(0,0,0,.18)}
.hanger--hero{left:235px;top:47px;--hole:var(--stage)}
.hanger--front{left:119px;top:641px;--hole:var(--paper)}
.hanger--back{left:398px;top:641px;--hole:var(--paper)}
.die-top{position:absolute;left:0;top:0;width:214px;height:95px;display:block}
.abs{position:absolute}
.photo{position:absolute;left:0;top:88px;width:214px;height:180px;
  background:linear-gradient(160deg,#d9dee4 0%,#c3cad2 30%,#6b6f74 55%,#3f4954 75%,#2d3a4a 100%);
  clip-path:polygon(0 0,100% 0,100% 77%,50% 100%,0 77%)}
.chevron{position:absolute;left:0;top:222px;width:214px;height:50px}
.brand{position:absolute;left:0;width:214px;text-align:center;font-weight:700;color:var(--ink);line-height:1.05}
.brand-name{font-size:15px;letter-spacing:2px}
.brand-sub{font-size:6.5px;letter-spacing:1.6px}
.brand .mark{display:inline-block;width:7px;height:7px;background:var(--blue);margin-right:4px;vertical-align:1px}
.headline{position:absolute;left:0;width:214px;text-align:center;font-weight:800;line-height:1}
.h-small{top:270px;font-size:16px}
.h-big{top:281px;font-size:46px;font-weight:900;color:var(--red);letter-spacing:-1px}
.h-mid{top:325px;font-size:13.5px}
.rule{position:absolute;left:12px;top:344px;width:190px;height:1px;background:#cfcfcf}
.rule-pill{position:absolute;left:85px;top:342px;width:44px;height:4px;border-radius:2px;background:var(--blue)}
.warranty{position:absolute;left:0;top:353px;width:214px;text-align:center;font-size:7.4px;font-weight:700}
.warranty b{color:var(--blue)}
.panel{position:absolute;left:17px;width:180px;border-radius:9px;background:var(--blue);color:var(--white)}
.panel--red{background:var(--red)}
.tab{position:absolute;height:17px;border-radius:9px 9px 0 0;background:var(--red);color:var(--white);font-weight:700;font-size:8.6px;text-align:center;line-height:17px}
.tab--blue{background:var(--blue)}
.services{position:absolute;left:29px;top:394px;display:grid;grid-template-columns:86px 86px;row-gap:2px;color:var(--white);font-size:6.4px;font-weight:700}
.services li,.ticks li{list-style:none;display:flex;align-items:center;gap:4px;height:8.8px}
.services svg{width:8px;height:7px;flex:none}
.badges{position:absolute;left:0;top:450px;width:214px;display:flex;justify-content:center;align-items:center;gap:10px}
.badge{width:24px;height:22px}
.footer{position:absolute;left:0;top:477px;width:214px;height:47px;background:var(--black)}
.call{position:absolute;left:45px;top:0;width:124px;height:17px;border-radius:0 0 10px 10px;background:var(--red);color:var(--white);font-weight:700;font-size:8px;text-align:center;line-height:17px}
.site{position:absolute;left:0;top:23px;width:214px;text-align:center;color:var(--white);font-size:8.6px;font-weight:500;letter-spacing:1px}
.site b{font-weight:700}
.neighbour{position:absolute;left:0;top:10px;width:214px;text-align:center;color:var(--white);font-weight:700;font-size:7.6px}
.free{position:absolute;left:0;top:142px;width:214px;text-align:center;color:var(--red);font-weight:800;font-size:16.5px}
.ticks{position:absolute;color:var(--white);font-size:6.6px;font-weight:700}
.ticks li{height:12px}
.ticks svg{width:5px;height:5px;flex:none}
.thumb{position:absolute;border:1px solid var(--white);border-radius:3px}
.offer{position:absolute;left:20px;top:402px;width:174px;text-align:center;font-size:4.3px;font-weight:600;line-height:1.3;color:var(--ink);z-index:2}
.roof-photo{position:absolute;left:0;top:398px;width:214px;height:79px;
  background:linear-gradient(180deg,#e6ecf1 0%,#dfe6ea 25%,#d9835a 55%,#b85a32 80%,#8a4a32 100%)}
</style>
</head>
<body>
<svg width="0" height="0" style="position:absolute" aria-hidden="true">
  <symbol id="i-house" viewBox="0 0 8 7"><path d="M0.5 3.5 4 0.6 7.5 3.5M1.5 2.8V6.5H6.5V2.8" fill="none" stroke="#fff" stroke-width=".8"/></symbol>
  <symbol id="i-tick" viewBox="0 0 10 10"><circle cx="5" cy="5" r="5" fill="#fff"/><path d="M2.8 5.2 4.4 6.7 7.3 3.5" fill="none" stroke="#0667be" stroke-width="1.4"/></symbol>
</svg>

<div class="stage-top"></div>

<!-- Front side, shown on the upper stage -->
<section class="hanger hanger--hero">
  <svg class="die-top" viewBox="0 0 214 95">
    <rect width="214" height="95" fill="var(--blue)"/>
    <path d="M0 89 L107 60 L214 89 L214 95 L0 95Z" fill="var(--white)"/>
    <path d="M0 86 L107 57 L214 86 L214 90 L107 61 L0 90Z" fill="var(--red)"/>
    <path d="M0 43 Q0 50 10 50 L95 50 L95 62 L10 62 Q0 62 0 70Z" fill="var(--hole)"/>
    <circle cx="108" cy="56" r="32" fill="var(--hole)"/>
  </svg>
  <div class="photo" role="img" aria-label="Photo of two roofers in hard hats installing shingles on a roof"></div>
  <svg class="chevron" viewBox="0 0 214 50"><path d="M0 3 L107 44 L214 3" fill="none" stroke="var(--blue)" stroke-width="4"/></svg>
  <div class="brand" style="top:96px"><div class="brand-name"><span class="mark"></span>PELLMONT</div><div class="brand-sub">ROOFING &amp; SIDING</div></div>
  <div class="headline h-small">RAISED ON</div>
  <div class="headline h-big">CARE</div>
  <div class="headline h-mid">PROVEN THROUGH SEASONS</div>
  <div class="rule"></div><div class="rule-pill"></div>
  <div class="warranty"><b>25 YEAR</b> LABOUR WARRANTY'S AVAILABLE</div>
  <div class="panel" style="top:376px;height:68px"></div>
  <div class="tab" style="left:40px;top:370px;width:134px">SERVICES WE OFFER</div>
  <ul class="services">
    <li><svg><use href="#i-house"/></svg>Roofing</li><li><svg><use href="#i-house"/></svg>Gutters &amp; Metals</li>
    <li><svg><use href="#i-house"/></svg>Repairs</li><li><svg><use href="#i-house"/></svg>Ventilation</li>
    <li><svg><use href="#i-house"/></svg>Siding</li><li><svg><use href="#i-house"/></svg>Inspections</li>
    <li><svg><use href="#i-house"/></svg>Strom damage</li><li><svg><use href="#i-house"/></svg>Other services</li>
  </ul>
  <div class="badges">
    <svg class="badge" viewBox="0 0 24 22" role="img" aria-label="Guild membership badge"><circle cx="12" cy="11" r="9" fill="var(--blue)"/></svg>
    <svg class="badge" viewBox="0 0 24 22" style="width:40px" role="img" aria-label="Accreditation badge"><rect x="1" y="4" width="38" height="15" rx="2" fill="#0f4d6e"/></svg>
    <svg class="badge" viewBox="0 0 24 22" role="img" aria-label="Contractor certification badge"><path d="M12 1 22 11 12 21 2 11Z" fill="#1d3f8a"/></svg>
    <svg class="badge" viewBox="0 0 24 22" style="width:36px" role="img" aria-label="Siding partner badge"><rect x="2" y="4" width="32" height="15" rx="2" fill="#2e8b3e"/></svg>
    <svg class="badge" viewBox="0 0 24 22" role="img" aria-label="32 years anniversary seal"><circle cx="12" cy="11" r="10" fill="#c9a227"/></svg>
  </div>
  <div class="footer"><div class="call">CALL US NOW: 403-555-0148</div><div class="site">www.<b>pellmontshingleworks</b>.com</div></div>
</section>

<!-- Front side, flat -->
<section class="hanger hanger--front">
  <svg class="die-top" viewBox="0 0 214 95">
    <rect width="214" height="95" fill="var(--blue)"/>
    <path d="M0 89 L107 60 L214 89 L214 95 L0 95Z" fill="var(--white)"/>
    <path d="M0 86 L107 57 L214 86 L214 90 L107 61 L0 90Z" fill="var(--red)"/>
    <path d="M0 43 Q0 50 10 50 L95 50 L95 62 L10 62 Q0 62 0 70Z" fill="var(--hole)"/>
    <circle cx="108" cy="56" r="32" fill="var(--hole)" stroke="#ddd" stroke-width=".6"/>
  </svg>
  <div class="photo" role="img" aria-label="Photo of two roofers in hard hats installing shingles on a roof"></div>
  <svg class="chevron" viewBox="0 0 214 50"><path d="M0 3 L107 44 L214 3" fill="none" stroke="var(--blue)" stroke-width="4"/></svg>
  <div class="brand" style="top:96px"><div class="brand-name"><span class="mark"></span>PELLMONT</div><div class="brand-sub">ROOFING &amp; SIDING</div></div>
  <div class="headline h-small">RAISED ON</div>
  <div class="headline h-big">CARE</div>
  <div class="headline h-mid">PROVEN THROUGH SEASONS</div>
  <div class="rule"></div><div class="rule-pill"></div>
  <div class="warranty"><b>25 YEAR</b> LABOUR WARRANTY'S AVAILABLE</div>
  <div class="panel" style="top:376px;height:68px"></div>
  <div class="tab" style="left:40px;top:370px;width:134px">SERVICES WE OFFER</div>
  <ul class="services">
    <li><svg><use href="#i-house"/></svg>Roofing</li><li><svg><use href="#i-house"/></svg>Gutters &amp; Metals</li>
    <li><svg><use href="#i-house"/></svg>Repairs</li><li><svg><use href="#i-house"/></svg>Ventilation</li>
    <li><svg><use href="#i-house"/></svg>Siding</li><li><svg><use href="#i-house"/></svg>Inspections</li>
    <li><svg><use href="#i-house"/></svg>Strom damage</li><li><svg><use href="#i-house"/></svg>Other services</li>
  </ul>
  <div class="badges">
    <svg class="badge" viewBox="0 0 24 22" role="img" aria-label="Guild membership badge"><circle cx="12" cy="11" r="9" fill="var(--blue)"/></svg>
    <svg class="badge" viewBox="0 0 24 22" style="width:40px" role="img" aria-label="Accreditation badge"><rect x="1" y="4" width="38" height="15" rx="2" fill="#0f4d6e"/></svg>
    <svg class="badge" viewBox="0 0 24 22" role="img" aria-label="Contractor certification badge"><path d="M12 1 22 11 12 21 2 11Z" fill="#1d3f8a"/></svg>
    <svg class="badge" viewBox="0 0 24 22" style="width:36px" role="img" aria-label="Siding partner badge"><rect x="2" y="4" width="32" height="15" rx="2" fill="#2e8b3e"/></svg>
    <svg class="badge" viewBox="0 0 24 22" role="img" aria-label="32 years anniversary seal"><circle cx="12" cy="11" r="10" fill="#c9a227"/></svg>
  </div>
  <div class="footer"><div class="call">CALL US NOW: 403-555-0148</div><div class="site">www.<b>pellmontshingleworks</b>.com</div></div>
</section>

<!-- Back side, flat -->
<section class="hanger hanger--back">
  <svg class="die-top" viewBox="0 0 214 95">
    <rect width="214" height="95" fill="var(--blue)"/>
    <path d="M0 89 L107 60 L214 89 L214 95 L0 95Z" fill="var(--white)"/>
    <path d="M0 88 L30 88 L107 60 L184 88 L214 88 L214 91 L0 91Z" fill="var(--red)"/>
    <path d="M55 88 L107 67 L159 88Z" fill="var(--red)"/>
    <path d="M214 43 Q214 49 204 49 L120 49 L120 61 L204 61 Q214 61 214 69Z" fill="var(--hole)"/>
    <circle cx="107" cy="55" r="32" fill="var(--hole)" stroke="#ddd" stroke-width=".6"/>
  </svg>
  <div class="neighbour">WE'RE IN YOUR NEIGHBOURHOOD!</div>
  <div class="brand" style="top:104px"><div class="brand-name"><span class="mark"></span>PELLMONT</div><div class="brand-sub">ROOFING &amp; SIDING</div></div>
  <div class="free">FREE ESTIMATES</div>

  <div class="panel" style="top:168px;height:64px"></div>
  <div class="tab" style="left:58px;top:164px;width:98px">ROOFING</div>
  <ul class="ticks" style="left:29px;top:187px">
    <li><svg><use href="#i-tick"/></svg>Asphalt</li><li><svg><use href="#i-tick"/></svg>Rubber</li><li><svg><use href="#i-tick"/></svg>Metal</li>
  </ul>
  <div class="thumb" style="left:133px;top:182px;width:58px;height:43px;background:linear-gradient(160deg,#9fb4c8,#5d7083 60%,#3a4450)" role="img" aria-label="Photo of a roofer working on a metal roof"></div>

  <div class="panel panel--red" style="top:244px;height:68px"></div>
  <div class="tab tab--blue" style="left:58px;top:238px;width:98px">SIDING</div>
  <div class="thumb" style="left:30px;top:258px;width:58px;height:46px;background:linear-gradient(180deg,#e9eef2 0%,#cfd6dc 50%,#4b4f55 100%)" role="img" aria-label="Photo of a house roof with a worker on top"></div>
  <ul class="ticks" style="left:95px;top:257px;font-size:6.3px">
    <li style="height:11px"><svg><use href="#i-tick"/></svg>Owen Brisket fibre cement</li><li style="height:11px"><svg><use href="#i-tick"/></svg>Vinyl</li>
    <li style="height:11px"><svg><use href="#i-tick"/></svg>Metal (steel, Aluminum)</li><li style="height:11px"><svg><use href="#i-tick"/></svg>Longboard</li>
  </ul>

  <div class="panel" style="top:324px;height:73px"></div>
  <div class="tab" style="left:48px;top:318px;width:118px">FULL EXTERIORS</div>
  <ul class="ticks" style="left:29px;top:340px;font-size:6.2px">
    <li><svg><use href="#i-tick"/></svg>Eavestrough/soffit/ Fascia</li><li><svg><use href="#i-tick"/></svg>stone</li>
    <li><svg><use href="#i-tick"/></svg>Skylights</li><li><svg><use href="#i-tick"/></svg>Windows &amp; Doors.</li>
  </ul>
  <ul class="ticks" style="left:134px;top:340px;font-size:6.2px">
    <li><svg><use href="#i-tick"/></svg>Stucco</li><li><svg><use href="#i-tick"/></svg>Insulation</li>
    <li><svg><use href="#i-tick"/></svg>Painting</li><li><svg><use href="#i-tick"/></svg>Shake Repairs</li>
  </ul>

  <div class="roof-photo" role="img" aria-label="Photo of a roofer repairing a clay tile roof"></div>
  <p class="offer">We are in your area, contact us today for your Exclusive limited time offer" *discounts apply exclusively to new agreements only</p>
  <div class="footer"><div class="call">CALL US NOW: 403-555-0148</div><div class="site">www.<b>pellmontshingleworks</b>.com</div></div>
</section>
</body>
</html>
```